Branding Package for an environmental water treatment operations company
Use the provided Logo. The name of the company is Coordinated Ecological Solutions or CES
Branding Package for an environmental water treatment operations company - Environment
Creative Brief
Professional
Mark Tellan
President
217 Halvering Ave Marlowton, PA. 15482
mktellan@postvale.com
U have freedom to experiment with any fonts to find the best match.
I will add to this later as I see what's being submitted.

```html
<!DOCTYPE html>
<html lang="en">
<head>
<meta charset="utf-8">
<title>Coordinated Ecological Solutions Stationery Concept</title>
<link href="https://fonts.googleapis.com/css2?family=Titillium+Web:ital,wght@0,400;0,700;1,400&family=Great+Vibes&display=swap" rel="stylesheet">
<style>
:root{
  --bg:#1c1917;
  --paper:#f6f6f4;
  --blue:#2b3cc0;
  --navy:#16207a;
  --green:#7db21b;
  --lime:#b8d21f;
  --ink:#2a2f6e;
  --grey:#8a8c94;
  --rule:#c9ccd6;
}
*{box-sizing:border-box;margin:0;padding:0}
html,body{width:1200px;height:370px;overflow:hidden;background:var(--bg)}
body{position:relative;font-family:"Titillium Web",sans-serif;color:var(--ink)}
.item{position:absolute;overflow:hidden}
.paper{background:var(--paper)}
.blue{background:linear-gradient(135deg,var(--navy),var(--blue) 60%,#3b52d8)}
.green{background:linear-gradient(135deg,#5f9414,var(--green) 55%,var(--lime))}
.caption{position:absolute;font-size:3px;font-style:italic;color:var(--grey);white-space:nowrap}

/* name lockup: circle + company name */
.mark{position:absolute;display:flex;align-items:center;gap:.18em;font-weight:700;color:var(--blue);line-height:1}
.mark::before{content:"";flex:none;width:.7em;height:.7em;border-radius:50%;background:var(--green)}
.mark .name{font-size:.36em;line-height:1.05;white-space:nowrap}
.mark.rev{color:#fff}
.mark.rev::before{background:#fff}

.intro .mark{font-size:22px;color:#fff;left:0;top:0}
.intro .mark::before{background:var(--green)}
.intro .tag{position:absolute;left:6px;top:26px;font-size:4px;color:#b9b9b9;letter-spacing:.15em}

.tiny{position:absolute;font-size:2.2px;line-height:1.35;color:var(--ink)}
.footer{position:absolute;left:0;right:0;bottom:3px;text-align:center;font-size:2.2px;line-height:1.4;color:var(--ink)}
.band{position:absolute;left:0;right:0;bottom:0;height:1.5px;background:var(--blue)}

/* slides */
.slide .title{position:absolute;left:6px;top:6px;font-size:5px;font-weight:700;color:var(--blue)}
.slide .sub{position:absolute;left:6px;top:13px;font-size:2.4px;font-style:italic;color:var(--ink)}
.slide ul{position:absolute;left:8px;top:18px;width:58%;font-size:2.1px;line-height:1.45;color:var(--ink)}
.slide .mark{font-size:5px;right:5px;top:6px}
.chart{position:absolute;right:8px;bottom:12px;display:flex;gap:2px;align-items:flex-end}
.chart span{width:4px;border:.4px solid var(--blue);border-bottom:none}
.specs{position:absolute;left:6px;top:17px;right:6px;font-size:2px;border-collapse:collapse;color:var(--ink)}
.specs td{padding:.3px 1px;border-bottom:.3px solid var(--rule)}
.boxes{position:absolute;left:6px;right:6px;top:30px;display:flex;gap:2px}
.boxes span{flex:1;height:16px;border:.4px solid var(--rule);font-size:2px;display:flex;align-items:center;justify-content:center;color:var(--blue)}

/* fax */
.fax table{position:absolute;left:9px;right:9px;top:31px;font-size:2.4px;border-collapse:collapse}
.fax td{border:.3px solid var(--rule);padding:.6px 1px;height:5px}
.fax td.l{width:14%;font-weight:700}
.fax .checks{position:absolute;left:9px;right:9px;top:56px;display:flex;justify-content:space-between;font-size:2.2px}
.fax .checks span::before{content:"";display:inline-block;width:2px;height:2px;border:.3px solid var(--ink);margin-right:.6px}
.fax .label{position:absolute;right:10px;top:23px;font-size:3px;font-weight:700}

.disc{position:absolute;border-radius:50%;overflow:hidden}
.disc::after{content:"";position:absolute;left:50%;top:50%;width:22%;height:22%;margin:-11% 0 0 -11%;border-radius:50%;background:var(--bg);box-shadow:0 0 0 2px #555}
.magnet{position:absolute;border-radius:50%;overflow:hidden}

.garment{position:absolute;width:58px;height:76px;border-radius:6px 6px 2px 2px}
.lines{position:absolute;left:4px;right:4px;top:14px;bottom:8px;background:repeating-linear-gradient(#fff 0 3px,var(--rule) 3px 3.3px)}
</style>
</head>
<body>

<!-- intro -->
<div class="item intro" style="left:20px;top:35px;width:60px;height:34px">
  <div class="mark"><span class="name">Coordinated Ecological<br>Solutions</span></div>
  <div class="tag">Stationery Concept</div>
</div>

<!-- business cards -->
<div class="item blue" style="left:82px;top:18px;width:47px;height:27px"><div class="mark rev" style="font-size:8px;left:8px;top:9px"><span class="name">Coordinated Ecological<br>Solutions</span></div></div>
<div class="caption" style="left:92px;top:47px">Business Card Back Option-A</div>
<div class="item paper" style="left:82px;top:51px;width:47px;height:27px"><div class="mark" style="font-size:8px;left:8px;top:9px"><span class="name">Coordinated Ecological<br>Solutions</span></div></div>
<div class="caption" style="left:92px;top:80px">Business Card Back Option-B</div>
<div class="item paper" style="left:19px;top:84px;width:47px;height:27px">
  <div class="mark" style="font-size:6px;left:3px;top:10px"><span class="name">Coordinated Ecological<br>Solutions</span></div>
  <div class="tiny" style="right:3px;top:3px;font-weight:700">Mark Tellan</div>
  <div class="tiny" style="right:3px;top:12px;text-align:right">217 Halvering Ave<br>Marlowton, PA. 15482<br>(412) 555-0186<br>mktellan@postvale.com</div>
</div>
<div class="caption" style="left:29px;top:113px">Business Card Front Option-1</div>
<div class="item paper" style="left:82px;top:84px;width:47px;height:27px">
  <div class="tiny" style="left:3px;top:3px;font-weight:700">Mark Tellan</div>
  <div class="tiny" style="left:3px;top:9px">217 Halvering Ave<br>Marlowton, PA. 15482<br>(412) 555-0186<br>mktellan@postvale.com</div>
  <div class="mark" style="font-size:6px;right:3px;top:10px"><span class="name">Coordinated Ecological<br>Solutions</span></div>
</div>
<div class="caption" style="left:92px;top:113px">Business Card Front Option-2</div>
<div class="item blue" style="left:82px;top:117px;width:47px;height:27px"><div class="mark rev" style="font-size:8px;left:8px;top:9px"><span class="name">Coordinated Ecological<br>Solutions</span></div></div>
<div class="caption" style="left:94px;top:146px">Biz Card Back Option-C</div>
<div class="item green" style="left:82px;top:149px;width:47px;height:27px"><div class="mark rev" style="font-size:8px;left:8px;top:9px"><span class="name">Coordinated Ecological<br>Solutions</span></div></div>
<div class="caption" style="left:94px;top:178px">Biz Card Back Option-D</div>
<div class="item blue" style="left:12px;top:129px;width:27px;height:46px;border-radius:2px"><div class="mark rev" style="font-size:4.5px;left:3px;top:20px"><span class="name">Coordinated Ecological<br>Solutions</span></div></div>
<div class="caption" style="left:16px;top:177px">Business Card Back</div>
<div class="item paper" style="left:47px;top:129px;width:27px;height:46px">
  <div class="tiny" style="right:2px;top:2px;font-weight:700">Mark Tellan</div>
  <div class="mark" style="font-size:4.5px;left:3px;top:16px"><span class="name">Coordinated Ecological<br>Solutions</span></div>
  <div class="tiny" style="left:3px;top:28px;text-align:center;width:21px">217 Halvering Ave<br>Marlowton, PA. 15482<br>(412) 555-0186</div>
</div>
<div class="caption" style="left:49px;top:177px">Business Card Front</div>

<!-- letterheads -->
<div class="item paper" style="left:137px;top:18px;width:112px;height:158px">
  <div class="mark" style="font-size:11px;right:7px;top:8px"><span class="name">Coordinated Ecological<br>Solutions</span></div>
  <div class="footer">217 Halvering Ave Marlowton, PA. 15482<br>T: (412) 555-0186 | F: (724) 555-0142 | mktellan@postvale.com | W: www.coordeco.com</div>
  <div class="band"></div>
</div>
<div class="caption" style="left:186px;top:177px">Letter Head -A</div>
<div class="item paper" style="left:257px;top:18px;width:112px;height:158px">
  <div class="mark" style="font-size:11px;left:34px;top:8px"><span class="name">Coordinated Ecological<br>Solutions</span></div>
  <div class="footer">217 Halvering Ave Marlowton, PA. 15482<br>(412) 555-0186 · (724) 555-0142 · mktellan@postvale.com · www.coordeco.com</div>
  <div class="band"></div>
</div>
<div class="caption" style="left:306px;top:177px">Letter Head -B</div>

<!-- envelopes -->
<div class="item paper" style="left:376px;top:18px;width:115px;height:19px;border-radius:0 0 10px 10px"><div class="mark" style="font-size:5px;left:48px;top:6px"><span class="name">Coordinated Ecological<br>Solutions</span></div></div>
<div class="item green" style="left:380px;top:40px;width:111px;height:18px"><div class="mark rev" style="font-size:5px;left:46px;top:6px"><span class="name">Coordinated Ecological<br>Solutions</span></div></div>
<div class="item paper" style="left:384px;top:61px;width:115px;height:54px"><div class="blue" style="position:absolute;left:0;right:0;top:0;height:18px"></div><div class="mark rev" style="font-size:5px;left:48px;top:6px"><span class="name">Coordinated Ecological<br>Solutions</span></div></div>
<div class="caption" style="left:428px;top:117px">Envelope Back</div>
<div class="item paper" style="left:376px;top:126px;width:115px;height:50px">
  <div class="mark" style="font-size:10px;left:6px;top:8px"><span class="name">Coordinated Ecological<br>Solutions</span></div>
  <div class="tiny" style="left:4px;bottom:4px">217 Halvering Ave Marlowton, PA. 15482</div>
</div>
<div class="caption" style="left:427px;top:177px">Envelope Front</div>

<!-- folder -->
<div class="item blue" style="left:507px;top:14px;width:104px;height:166px">
  <div class="mark rev" style="font-size:6px;left:38px;top:90px"><span class="name">Coordinated Ecological<br>Solutions</span></div>
  <div class="tiny" style="left:30px;top:108px;color:#fff;text-align:center;width:44px">217 Halvering Ave Marlowton, PA. 15482<br>(412) 555-0186 · (724) 555-0142<br>mktellan@postvale.com</div>
  <div class="item paper" style="left:31px;top:131px;width:48px;height:26px">
    <div class="mark" style="font-size:5px;left:3px;top:10px"><span class="name">Coordinated Ecological<br>Solutions</span></div>
    <div class="tiny" style="right:2px;top:3px;text-align:right">Mark Tellan<br>President<br>(412) 555-0186<br>mktellan@postvale.com</div>
  </div>
</div>
<div class="item paper" style="left:611px;top:14px;width:104px;height:120px">
  <div class="mark" style="font-size:18px;left:20px;top:48px"><span class="name">Coordinated Ecological<br>Solutions</span></div>
  <div class="tiny" style="left:33px;top:110px;font-size:2.4px">● www.coordeco.com</div>
</div>
<div class="item blue" style="left:611px;top:134px;width:104px;height:46px"></div>
<div class="caption" style="left:596px;top:182px">Folder / Cover File "Front n Back"</div>

<!-- presentation -->
<div class="item paper slide" style="left:723px;top:18px;width:99px;height:74px">
  <div style="position:absolute;left:0;right:0;top:9px;text-align:center;font-size:6px;font-weight:700;color:var(--blue)">WELCOME</div>
  <div class="mark" style="font-size:13px;left:26px;top:20px"><span class="name">Coordinated Ecological<br>Solutions</span></div>
  <div style="position:absolute;left:0;right:0;top:47px;text-align:center;font-size:6px;font-style:italic;color:var(--ink)">Presentation Title</div>
  <div style="position:absolute;left:0;right:0;top:56px;text-align:center;font-size:2.4px;font-style:italic;line-height:1.4">Clean water operations for every<br>community we serve</div>
</div>
<div class="item paper slide" style="left:831px;top:18px;width:99px;height:74px">
  <div class="title">Sub Title Lorem Ipsum<br>1999-2015</div><div class="mark"><span class="name">Coordinated Ecological<br>Solutions</span></div>
  <div class="sub" style="top:20px">Sub Title Lorem Ipsum</div>
  <ul style="top:25px"><li>Plant treatment output rose each year</li><li>Discharge quality met state limits</li><li>Field crews grew across the region</li><li>Sludge handling costs were reduced</li><li>New monitoring sites were added</li></ul>
  <div class="chart"><span style="height:8px"></span><span style="height:12px"></span><span style="height:18px"></span><span style="height:24px"></span><span style="height:30px"></span><span style="height:36px"></span></div>
</div>
<div class="item paper slide" style="left:940px;top:18px;width:99px;height:74px">
  <div class="title">Sub Title Lorem Ipsum</div><div class="mark"><span class="name">Coordinated Ecological<br>Solutions</span></div>
  <div class="sub">Sub Title Lorem Ipsum</div>
  <table class="specs"><tr><td>Intake volume</td><td>Daily flow</td><td>XXX.XX</td></tr><tr><td>Filtration</td><td>Media beds</td><td>X.XX</td></tr><tr><td>Aeration</td><td>Basins</td><td>XX.XX</td></tr><tr><td>Clarifiers</td><td>Settling</td><td>XXX.XX</td></tr><tr><td>Disinfection</td><td>UV units</td><td>XXXX.XX</td></tr></table>
  <ul style="top:50px;width:86%"><li>Operators trained on every new system</li><li>Reports delivered monthly to clients</li></ul>
</div>
<div class="item paper slide" style="left:723px;top:102px;width:99px;height:74px">
  <div class="title">Sub Title Lorem Ipsum</div><div class="mark"><span class="name">Coordinated Ecological<br>Solutions</span></div>
  <div class="sub">Sub Title Lorem Ipsum</div>
  <ul style="width:86%"><li>Site audits begin each new contract</li><li>Plans are shared with the client team</li></ul>
  <div class="boxes"><span>Image</span><span>Image</span><span>Image</span></div>
  <ul style="top:52px;width:86%"><li>Crews start work within two weeks</li><li>Results are tracked on site daily</li></ul>
</div>
<div class="item paper slide" style="left:831px;top:102px;width:99px;height:74px">
  <div class="title">Sub Title Lorem Ipsum</div><div class="mark"><span class="name">Coordinated Ecological<br>Solutions</span></div>
  <div class="sub">Sub Title Lorem Ipsum</div>
  <ul style="width:86%"><li>Steady service for municipal plants</li><li>Support for industrial water users</li></ul>
  <svg style="position:absolute;left:8px;top:40px" width="34" height="26" viewBox="0 0 34 26"><g fill="none" stroke="var(--navy)" stroke-width=".7"><circle cx="5" cy="18" r="4.5"/><circle cx="14" cy="18" r="4.5"/><circle cx="23" cy="18" r="4.5"/><circle cx="9" cy="9" r="4"/><circle cx="19" cy="9" r="4"/><circle cx="3" cy="3" r="1.5"/></g></svg>
  <ul style="left:52px;top:44px;width:40%"><li>Testing</li><li>Reporting</li><li>Permits</li></ul>
</div>
<div class="item blue slide" style="left:940px;top:102px;width:99px;height:74px">
  <div style="position:absolute;left:0;right:0;top:10px;text-align:center;font-size:8px;font-style:italic;color:#fff">Thanks You</div>
  <div style="position:absolute;left:0;right:0;top:24px;text-align:center;font-size:2.4px;font-style:italic;color:#fff;line-height:1.4">Thank you for your time and<br>for trusting our crews</div>
  <div class="mark rev" style="font-size:6px;left:37px;top:45px"><span class="name">Coordinated Ecological<br>Solutions</span></div>
  <div class="tiny" style="left:0;right:0;top:60px;text-align:center;color:#fff">217 Halvering Ave Marlowton, PA. 15482<br>(412) 555-0186 · www.coordeco.com</div>
</div>

<!-- magnets -->
<div class="magnet blue" style="left:1046px;top:28px;width:30px;height:30px"><div class="mark rev" style="font-size:5px;left:6px;top:12px"><span class="name">Coordinated Ecological<br>Solutions</span></div></div>
<div class="caption" style="left:1046px;top:59px">Refrigerator Magnets : Option-A</div>
<div class="magnet green" style="left:1046px;top:64px;width:30px;height:30px"><div class="mark rev" style="font-size:5px;left:6px;top:12px"><span class="name">Coordinated Ecological<br>Solutions</span></div></div>
<div class="magnet blue" style="left:1046px;top:100px;width:30px;height:30px"><div class="mark rev" style="font-size:5px;left:6px;top:12px"><span class="name">Coordinated Ecological<br>Solutions</span></div></div>
<div class="magnet green" style="left:1046px;top:136px;width:30px;height:30px"><div class="mark rev" style="font-size:5px;left:6px;top:12px"><span class="name">Coordinated Ecological<br>Solutions</span></div></div>

<!-- notepad -->
<div class="item blue" style="left:1086px;top:20px;width:47px;height:76px"><div class="mark rev" style="font-size:6px;left:11px;top:56px"><span class="name">Coordinated Ecological<br>Solutions</span></div></div>
<div class="item paper" style="left:1086px;top:101px;width:47px;height:73px"><div class="mark" style="font-size:5px;left:12px;top:4px"><span class="name">Coordinated Ecological<br>Solutions</span></div><div class="lines"></div></div>
<div class="caption" style="left:1100px;top:175px">Note Pad : Inside</div>

<!-- mug prints -->
<div class="item blue" style="left:1145px;top:20px;width:34px;height:32px;border-radius:3px"><div class="mark rev" style="font-size:5px;left:7px;top:13px"><span class="name">Coordinated Ecological<br>Solutions</span></div></div>
<div class="item paper" style="left:1145px;top:58px;width:34px;height:32px;border-radius:3px"><div class="mark" style="font-size:5px;left:7px;top:13px"><span class="name">Coordinated Ecological<br>Solutions</span></div></div>
<div class="item blue" style="left:1145px;top:98px;width:34px;height:32px;border-radius:3px"><div class="mark rev" style="font-size:5px;left:7px;top:13px"><span class="name">Coordinated Ecological<br>Solutions</span></div></div>
<div class="item paper" style="left:1145px;top:138px;width:34px;height:32px;border-radius:3px"><div class="mark" style="font-size:5px;left:7px;top:13px"><span class="name">Coordinated Ecological<br>Solutions</span></div></div>

<!-- USB -->
<div class="item blue" style="left:12px;top:192px;width:24px;height:10px;border-radius:2px"><div class="mark rev" style="font-size:4px;left:3px;top:3px"><span class="name">Coordinated Ecological<br>Solutions</span></div></div>
<div class="caption" style="left:26px;top:204px">USB Back Side</div>
<div class="caption" style="left:15px;top:213px">USB Front Side</div>
<div class="item paper" style="left:10px;top:218px;width:24px;height:9px;border-radius:2px"><div class="mark" style="font-size:4px;left:3px;top:2.5px"><span class="name">Coordinated Ecological<br>Solutions</span></div></div>

<!-- email signatures -->
<div class="item paper" style="left:56px;top:203px;width:30px;height:61px">
  <div class="mark" style="font-size:5px;left:3px;top:12px"><span class="name">Coordinated Ecological<br>Solutions</span></div>
  <div class="tiny" style="left:0;right:0;top:28px;text-align:center"><b>Mark Tellan</b><br>President<br><br>217 Halvering Ave<br>Marlowton, PA. 15482<br>(412) 555-0186<br>mktellan@postvale.com</div>
</div>
<div class="caption" style="left:58px;top:265px">E-mail Signature : Option-A</div>
<div class="item paper" style="left:33px;top:277px;width:76px;height:27px">
  <div class="tiny" style="left:3px;top:3px"><b>Mark Tellan</b><br>President<br><br>217 Halvering Ave<br>Marlowton, PA. 15482<br>(412) 555-0186<br>mktellan@postvale.com</div>
  <div class="mark" style="font-size:8px;right:5px;top:9px"><span class="name">Coordinated Ecological<br>Solutions</span></div>
</div>
<div class="caption" style="left:57px;top:305px">E-mail Signature : Option-B</div>
<div class="item paper" style="left:23px;top:323px;width:96px;height:24px">
  <div class="mark" style="font-size:8px;left:5px;top:8px"><span class="name">Coordinated Ecological<br>Solutions</span></div>
  <div class="tiny" style="right:3px;top:4px;text-align:right"><b>Mark Tellan</b><br>President<br>217 Halvering Ave Marlowton, PA. 15482<br>(412) 555-0186 | mktellan@postvale.com</div>
</div>
<div class="caption" style="left:57px;top:348px">E-mail Signature : Option-C</div>

<!-- CD cover and discs -->
<div class="item blue" style="left:96px;top:194px;width:64px;height:64px">
  <div class="mark rev" style="font-size:10px;left:10px;top:10px"><span class="name">Coordinated Ecological<br>Solutions</span></div>
  <div class="tiny" style="left:0;right:0;top:35px;text-align:center;color:#fff">217 Halvering Ave<br>Marlowton, PA. 15482<br>(412) 555-0186<br>mktellan@postvale.com<br>www.coordeco.com</div>
</div>
<div class="caption" style="left:121px;top:259px">CD/DVD Cover</div>
<div class="disc paper" style="left:165px;top:195px;width:60px;height:60px"><div class="mark" style="font-size:9px;left:13px;top:41px"><span class="name">Coordinated Ecological<br>Solutions</span></div></div>
<div class="caption" style="left:189px;top:259px">CD/DVD-1</div>
<div class="disc blue" style="left:231px;top:195px;width:60px;height:60px"><div class="mark rev" style="font-size:9px;left:13px;top:41px"><span class="name">Coordinated Ecological<br>Solutions</span></div></div>
<div class="caption" style="left:256px;top:259px">CD/DVD-2</div>
<div class="disc green" style="left:298px;top:195px;width:60px;height:60px"><div class="mark rev" style="font-size:9px;left:13px;top:41px"><span class="name">Coordinated Ecological<br>Solutions</span></div></div>
<div class="caption" style="left:323px;top:259px">CD/DVD-3</div>

<!-- thank you card -->
<div class="item paper" style="left:372px;top:190px;width:79px;height:46px">
  <div style="position:absolute;left:20px;top:6px;font-family:'Great Vibes',cursive;font-size:14px;color:var(--navy)">Thank you</div>
  <div class="mark" style="font-size:6px;left:27px;top:35px"><span class="name">Coordinated Ecological<br>Solutions</span></div>
</div>
<div class="caption" style="left:397px;top:240px">Thanks Post Card Folded : Front</div>
<div class="item blue" style="left:356px;top:246px;width:79px;height:46px">
  <div class="mark rev" style="font-size:8px;left:22px;top:16px"><span class="name">Coordinated Ecological<br>Solutions</span></div>
  <div class="tiny" style="left:0;right:0;top:30px;text-align:center;color:#fff">217 Halvering Ave Marlowton, PA. 15482<br>(412) 555-0186 · mktellan@postvale.com</div>
</div>
<div class="caption" style="left:380px;top:294px">Thanks Post Card Folded : Back</div>

<!-- screens -->
<div class="item blue" style="left:146px;top:292px;width:24px;height:52px;border-radius:2px"><div class="mark rev" style="font-size:4.5px;left:2px;top:22px"><span class="name">Coordinated Ecological<br>Solutions</span></div></div>
<div class="caption" style="left:152px;top:351px">Player</div>
<div class="item blue" style="left:190px;top:278px;width:86px;height:66px;border-radius:2px"><div class="mark rev" style="font-size:12px;left:12px;top:26px"><span class="name">Coordinated Ecological<br>Solutions</span></div></div>
<div class="caption" style="left:227px;top:351px">Tablet</div>
<div class="item blue" style="left:298px;top:282px;width:35px;height:58px;border-radius:2px"><div class="mark rev" style="font-size:6px;left:3px;top:24px"><span class="name">Coordinated Ecological<br>Solutions</span></div></div>
<div class="caption" style="left:310px;top:351px">Phone</div>

<!-- compliment slip -->
<div class="item paper" style="left:342px;top:297px;width:115px;height:53px">
  <div class="mark" style="font-size:11px;left:7px;top:8px"><span class="name">Coordinated Ecological<br>Solutions</span></div>
  <div style="position:absolute;right:8px;top:24px;font-size:4.2px;font-style:italic">With Compliments</div>
  <div style="position:absolute;right:8px;top:34px;width:52px;height:.5px;background:var(--ink)"></div>
  <div class="footer" style="bottom:3px">(412) 555-0186 | F: (724) 555-0142 | mktellan@postvale.com | W: www.coordeco.com</div>
  <div class="band"></div>
</div>
<div class="caption" style="left:388px;top:352px">With Compliment Slip</div>

<!-- fax -->
<div class="item paper fax" style="left:475px;top:193px;width:112px;height:157px">
  <div class="mark" style="font-size:11px;right:7px;top:8px"><span class="name">Coordinated Ecological<br>Solutions</span></div>
  <div class="label">FAX</div>
  <table><tr><td class="l">To:</td><td></td><td class="l">From:</td><td></td></tr><tr><td class="l">Fax:</td><td></td><td class="l">Pages:</td><td></td></tr><tr><td class="l">Phone:</td><td></td><td class="l">Date:</td><td></td></tr><tr><td class="l">Re:</td><td></td><td class="l">CC:</td><td></td></tr></table>
  <div class="checks"><span>Urgent</span><span>For Review</span><span>Please Comment</span><span>Please Reply</span><span>Please Recycle</span></div>
  <div class="tiny" style="left:9px;top:62px;font-weight:700">Comments</div>
  <div class="footer">217 Halvering Ave Marlowton, PA. 15482<br>T: (412) 555-0186 | F: (724) 555-0142 | mktellan@postvale.com | W: www.coordeco.com</div>
  <div class="band"></div>
</div>
<div class="caption" style="left:521px;top:352px">Fax Option-A</div>
<div class="item paper fax" style="left:594px;top:193px;width:112px;height:157px">
  <div class="mark" style="font-size:11px;left:34px;top:8px"><span class="name">Coordinated Ecological<br>Solutions</span></div>
  <div class="label">FAX</div>
  <table><tr><td class="l">To:</td><td></td><td class="l">From:</td><td></td></tr><tr><td class="l">Fax:</td><td></td><td class="l">Pages:</td><td></td></tr><tr><td class="l">Phone:</td><td></td><td class="l">Date:</td><td></td></tr><tr><td class="l">Re:</td><td></td><td class="l">CC:</td><td></td></tr></table>
  <div class="checks"><span>Urgent</span><span>For Review</span><span>Please Comment</span><span>Please Reply</span><span>Please Recycle</span></div>
  <div class="tiny" style="left:9px;top:62px;font-weight:700">Comments</div>
  <div class="footer">217 Halvering Ave Marlowton, PA. 15482<br>(412) 555-0186 · (724) 555-0142 · mktellan@postvale.com · www.coordeco.com</div>
  <div class="band"></div>
</div>
<div class="caption" style="left:640px;top:352px">Fax Option-B</div>

<!-- apparel, flat -->
<div class="garment" style="left:722px;top:195px;background:var(--blue)"><div class="mark rev" style="font-size:3px;left:36px;top:22px"><span class="name">Coordinated Ecological<br>Solutions</span></div></div>
<div class="garment" style="left:786px;top:195px;background:var(--blue)"><div class="mark rev" style="font-size:8px;left:8px;top:24px"><span class="name">Coordinated Ecological<br>Solutions</span></div></div>
<div class="garment" style="left:850px;top:195px;background:var(--green)"><div class="mark rev" style="font-size:8px;left:8px;top:24px"><span class="name">Coordinated Ecological<br>Solutions</span></div></div>
<div class="garment" style="left:914px;top:195px;background:var(--blue)"><div class="mark rev" style="font-size:8px;left:8px;top:24px"><span class="name">Coordinated Ecological<br>Solutions</span></div></div>
<div class="garment" style="left:978px;top:195px;background:#f2f2f2"><div class="mark" style="font-size:8px;left:8px;top:24px"><span class="name">Coordinated Ecological<br>Solutions</span></div></div>
<div class="garment" style="left:1042px;top:195px;background:#f2f2f2"><div class="mark" style="font-size:3px;left:34px;top:26px"><span class="name">Coordinated Ecological<br>Solutions</span></div></div>
<div class="garment" style="left:722px;top:278px;background:#f2f2f2"><div class="mark" style="font-size:3px;left:36px;top:22px"><span class="name">Coordinated Ecological<br>Solutions</span></div></div>
<div class="garment" style="left:786px;top:278px;background:#f2f2f2"><div class="mark" style="font-size:8px;left:8px;top:24px"><span class="name">Coordinated Ecological<br>Solutions</span></div></div>
<div class="garment" style="left:850px;top:278px;background:var(--green)"><div class="mark rev" style="font-size:3px;left:36px;top:22px"><span class="name">Coordinated Ecological<br>Solutions</span></div></div>
<div class="garment" style="left:914px;top:278px;background:var(--blue)"><div class="mark rev" style="font-size:3px;left:36px;top:22px"><span class="name">Coordinated Ecological<br>Solutions</span></div></div>
<div class="garment" style="left:978px;top:278px;background:#f2f2f2"><div class="mark" style="font-size:3px;left:36px;top:22px"><span class="name">Coordinated Ecological<br>Solutions</span></div></div>
<div class="garment" style="left:1042px;top:278px;background:var(--blue)"><div class="mark rev" style="font-size:3px;left:36px;top:22px"><span class="name">Coordinated Ecological<br>Solutions</span></div></div>
<div class="garment" style="left:1106px;top:278px;background:var(--green)"><div class="mark rev" style="font-size:3px;left:36px;top:22px"><span class="name">Coordinated Ecological<br>Solutions</span></div></div>

<!-- caps -->
<div class="item green" style="left:1108px;top:188px;width:36px;height:22px;border-radius:18px 18px 3px 3px"><div class="mark rev" style="font-size:4px;left:9px;top:9px"><span class="name">Coordinated Ecological<br>Solutions</span></div></div>
<div class="item" style="left:1152px;top:188px;width:36px;height:22px;border-radius:18px 18px 3px 3px;background:#f2f2f2"><div class="mark" style="font-size:4px;left:9px;top:9px"><span class="name">Coordinated Ecological<br>Solutions</span></div></div>
<div class="item blue" style="left:1108px;top:218px;width:36px;height:22px;border-radius:18px 18px 3px 3px"><div class="mark rev" style="font-size:4px;left:9px;top:9px"><span class="name">Coordinated Ecological<br>Solutions</span></div></div>
<div class="item" style="left:1152px;top:218px;width:36px;height:22px;border-radius:18px 18px 3px 3px;background:#f2f2f2"><div class="mark" style="font-size:4px;left:9px;top:9px"><span class="name">Coordinated Ecological<br>Solutions</span></div></div>
<div class="item green" style="left:1108px;top:248px;width:36px;height:22px;border-radius:18px 18px 3px 3px"><div class="mark rev" style="font-size:4px;left:9px;top:9px"><span class="name">Coordinated Ecological<br>Solutions</span></div></div>
<div class="item" style="left:1152px;top:248px;width:36px;height:22px;border-radius:18px 18px 3px 3px;background:#f2f2f2"><div class="mark" style="font-size:4px;left:9px;top:9px"><span class="name">Coordinated Ecological<br>Solutions</span></div></div>

</body>
</html>
```